Pellrow Strategies business card

I need a business card for my new strategic consulting LLC, Pellrow Strategies. We specialize in helping people who care about broadband technology and telecommunications policy, and we're based in Washington DC. I'm looking for a card that says smart, credible, future-facing and signals a high level of expertise. It's DC, so there's clearly a limit to how crazy we can go with this card, but I am looking for a design that reflects a company that is comfortable with technology, policy, and having a little bit fun. I'm uploading my logo below, and I'd like to have it be part of the card design in some fashion.
Target Market(s)
Telecommunications and technology policy professionals
Industry/Entity Type
Technology policy
Contact Information for Business Card
Name of business, my name (Colin Mabberly), email (colin@pellrowstrategies.example) , phone number (202-555-0148)phone number
Look and feel

```html
<!DOCTYPE html>
<html lang="en">
<head>
<meta charset="utf-8">
<title>Pellrow Strategies – Business Card</title>
<link href="https://fonts.googleapis.com/css2?family=Libre+Baskerville:wght@400;700&display=swap" rel="stylesheet">
<style>
  :root {
    --backdrop: #e6e7ea;
    --navy-deep: #0a2559;
    --navy-mid: #123f86;
    --brand-blue: #0f4295;
    --brand-gold: #eaa12c;
    --paper: #ffffff;
    --paper-shade: #eeeeef;
    --ink-grey: #4a4a4a;
  }
  * { box-sizing: border-box; margin: 0; padding: 0; }
  html, body {
    width: 1200px; height: 900px; overflow: hidden;
    background: var(--backdrop);
    font-family: "Libre Baskerville", Georgia, serif;
  }
  .canvas {
    width: 1200px; height: 900px;
    display: flex; flex-direction: column;
    align-items: center; justify-content: center;
    gap: 48px;
  }
  .card {
    width: 640px; height: 366px;
    border-radius: 34px;
    position: relative;
    overflow: hidden;
    box-shadow: 0 10px 28px rgba(0,0,0,.18);
  }
  .card-front {
    background: radial-gradient(ellipse at 40% 35%, var(--navy-mid) 0%, var(--navy-deep) 75%);
    display: flex; align-items: center; justify-content: center;
  }
  .card-back {
    background: linear-gradient(160deg, var(--paper) 40%, var(--paper-shade) 100%);
  }
  .brand-name {
    font-weight: 700;
    letter-spacing: .5px;
    white-space: nowrap;
  }
  .card-front .brand-name {
    color: var(--brand-gold);
    font-size: 44px;
  }
  .card-back .brand-name {
    position: absolute;
    top: 74px; left: 0; right: 0;
    text-align: center;
    color: var(--brand-blue);
    font-size: 38px;
  }
  .contact-row {
    position: absolute;
    left: 56px; right: 40px; bottom: 70px;
    display: flex; align-items: center; gap: 24px;
  }
  .holder-name {
    color: var(--brand-blue);
    font-size: 19px;
    text-transform: uppercase;
    letter-spacing: .5px;
    white-space: nowrap;
  }
  .divider {
    width: 2px; height: 62px;
    background: var(--brand-gold);
  }
  .contact-list { list-style: none; display: flex; flex-direction: column; gap: 12px; }
  .contact-list li {
    display: flex; align-items: center; gap: 10px;
    color: var(--ink-grey);
    font-size: 14px;
  }
  .contact-list svg { width: 16px; height: 16px; fill: var(--brand-blue); flex: none; }
</style>
</head>
<body>
<main class="canvas">
  <section class="card card-front" aria-label="Card front">
    <h1 class="brand-name">Pellrow Strategies</h1>
  </section>

  <section class="card card-back" aria-label="Card back">
    <h2 class="brand-name">Pellrow Strategies</h2>
    <div class="contact-row">
      <p class="holder-name">Colin Mabberly</p>
      <span class="divider"></span>
      <ul class="contact-list">
        <li>
          <svg viewBox="0 0 24 24" aria-hidden="true"><path d="M6.6 10.8a15.1 15.1 0 0 0 6.6 6.6l2.2-2.2a1 1 0 0 1 1-.25 11.4 11.4 0 0 0 3.6.57 1 1 0 0 1 1 1V20a1 1 0 0 1-1 1A17 17 0 0 1 3 4a1 1 0 0 1 1-1h3.5a1 1 0 0 1 1 1c0 1.25.2 2.45.57 3.57a1 1 0 0 1-.25 1z"/></svg>
          <span>202-555-0148</span>
        </li>
        <li>
          <svg viewBox="0 0 24 24" aria-hidden="true"><path d="M2 5h20v14H2z M3.5 6.5 12 13l8.5-6.5" fill="none" stroke="#0f4295" stroke-width="2"/></svg>
          <span>colin@pellrowstrategies.example</span>
        </li>
      </ul>
    </div>
  </section>
</main>
</body>
</html>
```